Business card design for an Art Director working for museums

The business card design we're looking for is for an Art Director in a private museum called "OLV Gallery". The museum showcases artworks made by the country's national artists. Designs should use the CMYK "0 40 100 20". You have the liberty to use any type you want except for overly decorative ones.

Target Market(s)

Professional and creative individuals. Interior designers, museum curators, museum coordinators etc

Industry/Entity Type

Museum

Contact Information for Business Card

Rel T
Art Director
+1 555 374 9281

Font styles to use
Serif
Sans Serif
Script

Requirements
Must have
• My project must have the CMYK 0 40 100 20. You can play with the Key.
• We're keen on clean, minimal, and architectural-type design.
Nice to have
• Geometric gradients that nicely complement the main CMYK that we've posted.
Should not have
• Off-putting colour palettes

```html
<!DOCTYPE html>
<html lang="en">
<head>
<meta charset="utf-8">
<title>OLV Gallery — Business Card</title>
<link rel="stylesheet" href="https://fonts.googleapis.com/css2?family=EB+Garamond:wght@400;600&display=swap">
<style>
  :root {
    --brand-amber: #C8830F;
    --card-white: #F7F6F3;
    --backdrop: #8E9093;
    --card-shadow: rgba(0, 0, 0, 0.28);
  }

  * { box-sizing: border-box; margin: 0; padding: 0; }

  html, body {
    width: 1200px;
    height: 1200px;
    overflow: hidden;
  }

  body {
    background: var(--backdrop);
    font-family: "EB Garamond", Garamond, serif;
    display: flex;
    flex-direction: column;
    align-items: center;
    justify-content: center;
    gap: 48px;
  }

  .card {
    position: relative;
    width: 840px;
    height: 480px;
    overflow: hidden;
    box-shadow: 0 14px 30px var(--card-shadow);
  }

  /* Front side */
  .card--front {
    background: var(--brand-amber);
  }

  .card--front .wordmark {
    position: absolute;
    left: 50%;
    top: 44%;
    transform: translate(-50%, -50%);
    color: var(--card-white);
    font-size: 64px;
  }

  .wordmark {
    font-family: "EB Garamond", Garamond, serif;
    font-weight: 400;
    letter-spacing: 0.04em;
    white-space: nowrap;
    display: flex;
    align-items: center;
    gap: 0.28em;
  }

  .wordmark__dot {
    width: 0.32em;
    height: 0.32em;
    border-radius: 50%;
    background: currentColor;
  }

  /* Back side */
  .card--back {
    background: var(--card-white);
  }

  .card__band {
    position: absolute;
    inset: 0;
    width: 100%;
    height: 100%;
  }

  .card__band polygon {
    fill: var(--brand-amber);
  }

  .card--back .wordmark {
    position: absolute;
    left: 88px;
    top: 96px;
    color: var(--brand-amber);
    font-size: 46px;
  }

  .contact {
    position: absolute;
    left: 470px;
    top: 206px;
    color: var(--brand-amber);
    font-size: 27px;
    line-height: 1.25;
  }

  .contact__name {
    font-weight: 600;
  }

  .contact__role {
    font-weight: 400;
  }

  .contact__phone {
    font-weight: 400;
    letter-spacing: 0.04em;
  }
</style>
</head>
<body>

  <section class="card card--front" aria-label="Card front">
    <div class="wordmark"><span class="wordmark__dot"></span>OLV Gallery</div>
  </section>

  <section class="card card--back" aria-label="Card back">
    <svg class="card__band" viewBox="0 0 840 480" preserveAspectRatio="none" aria-hidden="true">
      <polygon points="0,200 840,480 0,480"></polygon>
    </svg>

    <div class="wordmark"><span class="wordmark__dot"></span>OLV Gallery</div>

    <div class="contact">
      <p><span class="contact__name">Rel T</span> <span class="contact__role">/ Art Director</span></p>
      <p class="contact__phone">P : +1 555 374 9281</p>
    </div>
  </section>

</body>
</html>
```